Office Warming Party. I attached an image (blogger flyer) that you can use as an example, or you can create one from scratch. I just want it to look clean but stylish like the example (but still professional). Text:

(ps if there is too much text, you can take out the last line and just put brantleylawgroup.com)

BRANTLEY LAW GROUP (logo attached with the skyline image, I will provide a better quality logo but this will work for the proof)

OFFICE WARMING PARTY
FRI NOV 15 2013 7-10PM
2742 K Avenue, Suite 410
Sacramento

Full Hosted Bar / Cocktail Attire

Music by SF's Marcus Tilden (larger text)
Also feat. Neil Ashby & Vance
Catering by Orvo, Saffrel, and Tosaki

Also a birthday party for Darnell Brantley. Invite only. Please RSVP
at www.eventgather.example/events/847203615924318

BRANTLEY LAW GROUP specializes in personal injury and criminal law, visit our site
at www.brantleylawgroup.com or call (916) 555-2817 for more information

It's not letting me attach the flyers so I'm including links to them:
http://www.gigpostline.example/images/uploads/flyers/blogger_holiday_party.jpg

http://www.valleyclaimhelp.example (brantley law group is top left)

Target Market(s)

Professionals but also house music lovers

Industry/Entity Type

Catering

Font styles to use
Sans Serif

Requirements
Must have
• Logo and DJ name bold or bigger (Marcus Tilden)

```html
<!DOCTYPE html>
<html lang="en">
<head>
<meta charset="utf-8">
<title>Brantley Law Group – Office Warming Party</title>
<link rel="stylesheet" href="https://fonts.googleapis.com/css2?family=Oswald:wght@400;500&family=Gudea:wght@400;700&display=swap">
<style>
  :root {
    --red: #c8161d;
    --ink: #1f1f1f;
    --grey: #6e6e6e;
    --grey-light: #9a9a9a;
    --rule: #cfcfcf;
    --paper: #f4f4f4;
    --band: #ffffff;
  }
  * { margin: 0; padding: 0; box-sizing: border-box; }
  html, body { width: 849px; height: 1200px; overflow: hidden; background: var(--paper); }
  .flyer {
    position: relative;
    width: 849px; height: 1200px;
    overflow: hidden;
    font-family: "Gudea", "Trebuchet MS", sans-serif;
    color: var(--ink);
  }
  .backdrop {
    position: absolute; inset: 0;
    background:
      linear-gradient(135deg, transparent 30%, rgba(200,200,200,.35) 30%, rgba(200,200,200,.35) 42%, transparent 42%),
      linear-gradient(135deg, transparent 58%, rgba(200,200,200,.3) 58%, rgba(200,200,200,.3) 70%, transparent 70%),
      radial-gradient(circle at 40% 30%, #fafafa 0%, #ececec 100%);
  }
  .brand {
    position: absolute; left: 87px; top: 48px;
    font-family: "Oswald", "Arial Narrow", sans-serif;
    font-weight: 500; color: var(--red);
    line-height: 1; letter-spacing: -0.5px;
  }
  .brand-name { display: block; font-size: 44px; }
  .brand-sub { display: block; font-size: 33px; margin-top: 2px; }
  .rule {
    position: absolute; left: 102px; width: 645px; height: 2px;
    background: var(--rule);
  }
  .line {
    position: absolute; left: 0; right: 0; text-align: center;
    white-space: nowrap;
  }
  .headline {
    font-family: "Oswald", "Arial Narrow", sans-serif;
    font-weight: 400; color: var(--red); line-height: 1;
  }
  .headline-top { top: 186px; font-size: 108px; letter-spacing: 2px; }
  .headline-bottom { top: 276px; font-size: 92px; letter-spacing: 1px; }
  .date {
    top: 392px; font-family: "Oswald", "Arial Narrow", sans-serif;
    font-size: 56px; color: var(--grey); line-height: 1;
  }
  .address { top: 452px; font-size: 33px; color: var(--grey-light); font-weight: 700; }
  .address svg { vertical-align: -4px; margin-right: 4px; }
  .bar-attire { top: 548px; font-size: 38px; font-weight: 700; color: var(--ink); }
  .bar-attire svg { vertical-align: -6px; margin: 0 4px; }
  .music-by { top: 632px; font-size: 36px; font-weight: 700; }
  .music-by svg { vertical-align: -6px; margin-right: 10px; }
  .dj {
    top: 683px; font-size: 62px; font-weight: 700; color: var(--red); line-height: 1.1;
  }
  .featuring { top: 748px; font-size: 36px; font-weight: 700; color: var(--ink); }
  .featuring .muted { color: var(--grey-light); }
  .catering { top: 828px; font-size: 30px; font-weight: 700; color: var(--grey); }
  .catering svg { vertical-align: -6px; margin-right: 10px; }
  .catering strong { color: var(--ink); }
  .invite { top: 896px; font-size: 25px; font-weight: 700; color: var(--grey); }
  .invite svg { vertical-align: -4px; margin: 0 8px; }
  .invite strong { color: var(--ink); }
  .celebrants { top: 930px; font-size: 25px; font-weight: 700; color: var(--ink); }
  .celebrants .name { color: var(--red); }
  .rsvp { top: 982px; font-size: 27px; font-weight: 700; color: var(--grey); }
  .rsvp strong { color: var(--ink); }
  .about { top: 1042px; font-size: 21px; font-weight: 700; color: var(--ink); }
  .contact { top: 1071px; font-size: 19px; font-weight: 700; color: var(--red); }
  .contact span { color: var(--ink); }
  .footer-band {
    position: absolute; left: 0; right: 0; top: 1124px; height: 76px;
    background: var(--band);
    box-shadow: 0 -3px 6px rgba(0,0,0,.08);
  }
  .footer-brand {
    position: absolute; right: 40px; top: 26px;
    font-family: "Oswald", "Arial Narrow", sans-serif;
    font-size: 16px; color: var(--red); letter-spacing: 0.5px;
  }
</style>
</head>
<body>
<main class="flyer">
  <div class="backdrop" role="img" aria-label="Soft grey background with large faint diagonal decorative shapes"></div>

  <div class="brand">
    <span class="brand-name">BRANTLEY</span>
    <span class="brand-sub">LAW GROUP</span>
  </div>

  <div class="rule" style="top:165px"></div>
  <h1 class="line headline headline-top">OFFICE</h1>
  <div class="line headline headline-bottom">WARMING PARTY</div>
  <div class="rule" style="top:382px"></div>

  <p class="line date">FRI NOV 15 2013 7-10PM</p>
  <p class="line address"><svg width="18" height="26" viewBox="0 0 18 26"><path d="M9 0C4 0 0 4 0 9c0 7 9 17 9 17s9-10 9-17C18 4 14 0 9 0z" fill="var(--red)"/><circle cx="9" cy="9" r="3.5" fill="#fff"/></svg>2742 K Avenue, Suite 410, Sacramento</p>
  <div class="rule" style="top:510px"></div>

  <p class="line bar-attire">Full Hosted Bar<svg width="26" height="36" viewBox="0 0 26 36"><path d="M2 2h22c0 9-4 15-11 15S2 11 2 2z" fill="var(--red)"/><rect x="12" y="16" width="2.5" height="14" fill="var(--red)"/><rect x="5" y="30" width="16" height="3" fill="var(--red)"/></svg>Cocktail Attire</p>
  <div class="rule" style="top:610px"></div>

  <p class="line music-by"><svg width="44" height="32" viewBox="0 0 44 32"><rect x="1" y="6" width="42" height="24" rx="4" fill="var(--red)"/><circle cx="18" cy="18" r="8" fill="#fff"/><circle cx="18" cy="18" r="2" fill="var(--red)"/><rect x="32" y="10" width="3" height="14" fill="#fff"/></svg>Music by</p>
  <p class="line dj">SF’s Marcus Tilden</p>
  <p class="line featuring"><span class="muted">also feat.</span> Neil Ashby &amp; Vance</p>
  <div class="rule" style="top:807px"></div>

  <p class="line catering"><svg width="30" height="32" viewBox="0 0 30 32"><path d="M2 0v10c0 3 2 4 3.5 4V32h3V14c1.5 0 3.5-1 3.5-4V0h-2v9H8V0H6v9H4V0z" fill="var(--red)"/><path d="M20 0c4 0 7 5 7 11s-2 6-3 6V32h-4z" fill="var(--red)"/></svg>Catering by <strong>Orvo</strong>, <strong>Saffrel</strong>, and <strong>Tosaki</strong></p>
  <div class="rule" style="top:882px"></div>

  <p class="line invite">Invite only.<svg width="30" height="28" viewBox="0 0 30 28"><rect x="3" y="12" width="24" height="14" fill="var(--red)"/><rect x="3" y="17" width="24" height="2" fill="#fff"/><rect x="1" y="26" width="28" height="2" fill="var(--red)"/><rect x="8" y="5" width="2" height="7" fill="var(--red)"/><rect x="14" y="5" width="2" height="7" fill="var(--red)"/><rect x="20" y="5" width="2" height="7" fill="var(--red)"/></svg><strong>Also a Birthday Celebration for</strong></p>
  <p class="line celebrants"><span class="name">Darnell Brantley</span> (11/15) and <span class="name">Renata Ellison</span> (11/16)!</p>
  <div class="rule" style="top:978px"></div>

  <p class="line rsvp">RSVP at <strong>www.eventgather.example/events/847203615924318</strong></p>
  <div class="rule" style="top:1024px"></div>

  <p class="line about">BRANTLEY LAW GROUP specializes in personal injury and criminal law.</p>
  <p class="line contact">Visit <span>www.brantleylawgroup.com</span> or call <span>(916) 555-2817</span> for more information.</p>

  <footer class="footer-band">
    <span class="footer-brand">BRANTLEY LAW GROUP</span>
  </footer>
</main>
</body>
</html>
```